Need updated stationery design for chiropractic clinic

We recently moved our office and are looking to refresh our letterhead, business cards, presentation folder and envelopes. I tend to prefer simple, clean designs. We communicate with a lot of attorneys and want to exude professionalism. I have attached our logo and 2 additional versions (all white and white letters instead of grey).

Target Market(s)

Other medical professionals and attorneys. Business cards will go to patients as well.

Industry/Entity Type

Healthcare

```html
<!DOCTYPE html>
<html lang="en">
<head>
<meta charset="utf-8">
<title>Alderline Business Card</title>
<link rel="stylesheet" href="https://fonts.googleapis.com/css2?family=Figtree:wght@400;500;600;700&display=swap">
<style>
  :root {
    --page-bg: #e4e4e4;
    --card-bg: #ffffff;
    --brand-blue: #0499cf;
    --brand-teal: #3dbfc8;
    --ink: #1c1c1c;
  }
  html, body {
    margin: 0;
    padding: 0;
    width: 1200px;
    height: 900px;
    overflow: hidden;
    background: var(--page-bg);
    font-family: "Figtree", sans-serif;
  }
  .business-card {
    position: absolute;
    left: 100px;
    top: 164px;
    width: 1000px;
    height: 572px;
    background: var(--card-bg);
    overflow: hidden;
    box-shadow: 0 4px 14px rgba(0,0,0,0.18);
  }
  .holder {
    position: absolute;
    left: 48px;
    top: 108px;
  }
  .holder-name {
    margin: 0;
    font-size: 31px;
    font-weight: 700;
    letter-spacing: 0.2px;
    color: var(--brand-blue);
    line-height: 1.1;
  }
  .holder-name .first { color: var(--brand-teal); }
  .holder-role {
    margin: 6px 0 0;
    font-size: 25px;
    font-weight: 400;
    color: var(--ink);
  }
  .office-address {
    position: absolute;
    left: 50px;
    top: 218px;
    margin: 0;
    font-style: normal;
    font-size: 25px;
    line-height: 36px;
    color: var(--ink);
  }
  .contact-list {
    position: absolute;
    left: 50px;
    top: 326px;
    margin: 0;
    padding: 0;
    list-style: none;
    font-size: 25px;
    color: var(--ink);
  }
  .contact-list li {
    display: flex;
    align-items: center;
    height: 36px;
  }
  .contact-list svg {
    width: 24px;
    height: 24px;
    margin-right: 15px;
    fill: var(--brand-teal);
  }
  .brand {
    position: absolute;
    left: 520px;
    top: 106px;
    display: flex;
    align-items: center;
  }
  .brand-square {
    width: 78px;
    height: 78px;
    background: var(--brand-teal);
    margin-right: 22px;
  }
  .brand-name {
    font-size: 70px;
    font-weight: 600;
    color: var(--brand-blue);
    line-height: 1;
  }
  .footer-rule {
    position: absolute;
    left: 0;
    right: 0;
    top: 466px;
    height: 6px;
    background: var(--brand-teal);
  }
  .footer-band {
    position: absolute;
    left: 0;
    right: 0;
    top: 480px;
    bottom: 0;
    background: var(--brand-blue);
  }
</style>
</head>
<body>
  <div class="business-card">
    <div class="holder">
      <h1 class="holder-name"><span class="first">DARA</span> WELLFORD</h1>
      <p class="holder-role">Co-Founder</p>
    </div>

    <address class="office-address">
      Harbor Point 2100 Linden<br>
      Ave Suite 310
    </address>

    <ul class="contact-list">
      <li>
        <svg viewBox="0 0 24 24" aria-hidden="true"><path d="M6.6 10.8a15.1 15.1 0 0 0 6.6 6.6l2.2-2.2a1 1 0 0 1 1-.25 11.4 11.4 0 0 0 3.6.57 1 1 0 0 1 1 1V20a1 1 0 0 1-1 1A17 17 0 0 1 3 4a1 1 0 0 1 1-1h3.5a1 1 0 0 1 1 1c0 1.25.2 2.45.57 3.57a1 1 0 0 1-.25 1z"/></svg>
        555-014-2387
      </li>
      <li>
        <svg viewBox="0 0 24 24" aria-hidden="true"><path d="M2 5h20v14H2z M4 7v.4l8 5.2 8-5.2V7z" fill-rule="evenodd"/></svg>
        hello@alderline.com
      </li>
      <li>
        <svg viewBox="0 0 24 24" aria-hidden="true"><circle cx="12" cy="12" r="10"/><path d="M2 12h20M12 2c3 3.2 3 16.8 0 20M12 2c-3 3.2-3 16.8 0 20" stroke="#fff" stroke-width="1.4" fill="none"/></svg>
        www.alderline.com
      </li>
    </ul>

    <div class="brand">
      <div class="brand-square"></div>
      <span class="brand-name">Alderline</span>
    </div>

    <div class="footer-rule"></div>
    <div class="footer-band"></div>
  </div>
</body>
</html>
```